Varneck Bidding Business Cards Design Needed

I need a business card design that is modern looking - double sided (maybe just my logo on the back, but open to suggestions) - the overall design is up to you. I want it to be easy to read - not over the top flashy. I already have a company logo which I uploaded so that needs to be used. The colors of my logo are the colors I want on the card... so blue and gray (do need to match the logo colors).

Requirements
Must have
• Would like the card to be sleek, modern and easy to ready

```html
<!DOCTYPE html>
<html lang="en">
<head>
<meta charset="utf-8">
<title>Varneck Bidding – Business Cards</title>
<link rel="stylesheet" href="https://fonts.googleapis.com/css2?family=Open+Sans:wght@600;700;800&display=swap">
<style>
  :root {
    --brand-blue: #2a73bb;
    --brand-gray: #555659;
    --text-gray: #4a4a4a;
    --card-white: #ffffff;
    --card-dark: #464646;
    --backdrop: #a7a8ac;
    --faint-light: #cfcfd0;
    --faint-dark: #525252;
  }
  * { box-sizing: border-box; margin: 0; padding: 0; }
  html, body { width: 1200px; height: 1200px; overflow: hidden; }
  body {
    background: var(--backdrop);
    font-family: "Open Sans", Arial, sans-serif;
    position: relative;
  }
  .card {
    position: absolute;
    left: 161px;
    width: 904px;
    height: 502px;
    overflow: hidden;
  }
  .card--front { top: 91px; background: var(--card-white); }
  .card--back { top: 607px; background: var(--card-dark); height: 513px; }

  .faint-mark {
    position: absolute;
    width: 300px;
    height: 300px;
  }
  .card--front .faint-mark { left: 36px; top: 345px; background: var(--faint-light); }
  .card--back .faint-mark { left: 36px; top: -200px; background: var(--faint-dark); }

  .brand {
    position: absolute;
    display: flex;
    align-items: center;
    gap: 14px;
    font-weight: 800;
    white-space: nowrap;
  }
  .brand__square { display: block; background: var(--brand-blue); }
  .card--front .brand { left: 68px; top: 176px; font-size: 38px; color: var(--brand-blue); }
  .card--front .brand__square { width: 34px; height: 34px; }

  .person {
    position: absolute;
    right: 116px;
    top: 184px;
    text-align: right;
  }
  .person__name {
    font-size: 37px;
    font-weight: 700;
    line-height: 1.1;
    letter-spacing: 0.5px;
    color: var(--brand-gray);
  }
  .person__first { color: var(--brand-blue); }
  .person__title {
    margin-top: 6px;
    font-size: 20px;
    font-weight: 700;
    color: var(--text-gray);
  }
  .person__rule {
    position: absolute;
    left: 804px;
    top: 200px;
    width: 3px;
    height: 54px;
    background: var(--brand-blue);
  }

  .contacts {
    position: absolute;
    right: 70px;
    top: 340px;
    list-style: none;
  }
  .contacts__item {
    display: flex;
    justify-content: flex-end;
    align-items: center;
    gap: 22px;
    height: 37px;
    font-size: 20px;
    font-weight: 700;
    color: var(--text-gray);
  }
  .contacts__icon { width: 20px; height: 20px; flex: none; }
  .contacts__accent { color: var(--brand-blue); }

  .card--back .brand {
    left: 0; right: 0;
    top: 215px;
    justify-content: center;
    font-size: 60px;
    color: #ffffff;
  }
  .card--back .brand__square { width: 52px; height: 52px; }
  .tagline {
    position: absolute;
    left: 0; right: 0;
    top: 318px;
    text-align: center;
    font-size: 20px;
    font-weight: 700;
    color: #ffffff;
  }
</style>
</head>
<body>

  <section class="card card--front" aria-label="Business card front">
    <div class="faint-mark" aria-hidden="true"></div>

    <div class="brand">
      <span class="brand__square" aria-hidden="true"></span>
      <span class="brand__name">Varneck Bidding</span>
    </div>

    <div class="person">
      <p class="person__name"><span class="person__first">CORIN</span> MADDOX</p>
      <p class="person__title">Owner/President - Auctioneer</p>
    </div>
    <span class="person__rule" aria-hidden="true"></span>

    <ul class="contacts">
      <li class="contacts__item">
        <span>+61 455 203 618</span>
        <svg class="contacts__icon" viewBox="0 0 24 24" aria-hidden="true">
          <path fill="#555" d="M6.6 10.8a15.1 15.1 0 0 0 6.6 6.6l2.2-2.2a1 1 0 0 1 1-.25 11.4 11.4 0 0 0 3.6.57 1 1 0 0 1 1 1V20a1 1 0 0 1-1 1A17 17 0 0 1 3 4a1 1 0 0 1 1-1h3.5a1 1 0 0 1 1 1c0 1.25.2 2.45.57 3.57a1 1 0 0 1-.25 1z"/>
        </svg>
      </li>
      <li class="contacts__item">
        <span>varneckbidding@mail.com</span>
        <svg class="contacts__icon" viewBox="0 0 24 24" aria-hidden="true">
          <path fill="#555" d="M3 6h18v12H3z"/>
          <path fill="none" stroke="#fff" stroke-width="1.6" d="M3.5 6.5 12 13l8.5-6.5"/>
        </svg>
      </li>
      <li class="contacts__item">
        <span>http://<span class="contacts__accent">bidhaven</span>.com/</span>
        <svg class="contacts__icon" viewBox="0 0 24 24" aria-hidden="true">
          <g fill="none" stroke="#666" stroke-width="1.4">
            <circle cx="12" cy="12" r="9"/>
            <ellipse cx="12" cy="12" rx="4" ry="9"/>
            <path d="M3 12h18M4.5 7.5h15M4.5 16.5h15"/>
          </g>
        </svg>
      </li>
    </ul>
  </section>

  <section class="card card--back" aria-label="Business card back">
    <div class="faint-mark" aria-hidden="true"></div>
    <div class="brand">
      <span class="brand__square" aria-hidden="true"></span>
      <span class="brand__name">Varneck Bidding</span>
    </div>
    <p class="tagline">Improving Charity Auctions Nationwide</p>
  </section>

</body>
</html>
```